Business Card Design Project

Roofing Consultant firm needs business card design

R.T. Haverbrook & Co., Inc
Roofing Consultants and Contractors
Specializing in Construction Defect Litigation

4817 Willow Crest Ln.
San Diego, CA 92847
Licences:
CA 514728, AZ 907465, NV 0063512
www.rthaverbrook-example.com

Will need cards for 3 persons:
Robert T. Haverbrook - Principal Consultant
Kevin Sallow - Associate Expert
Marla Vinsett - Controller
ph-555-217-6400
fax -555-217-6402
Cell - (will be 3 different numbers)
Email - (will be 3 different addresses)
Attached graphic is what we had before..the RTH with the roof graphic has been our logo for awhile, but we are open to change.
Updates

I now see we will need to add an email field to the design.  Sorry I didnt think of it when I was setting this up.  Thank you for your submittals. They are all very good. 

Target Market(s)

Attorneys, Homeowner Associations, Insurance Carriers

Industry/Entity Type

Business

Requirements
Must have
• RTH logo roof design. (owner created)

```html
<!DOCTYPE html>
<html lang="en">
<head>
<meta charset="utf-8">
<title>R.T. Haverbrook &amp; Co., Inc – Business Card</title>
<link rel="stylesheet" href="https://fonts.googleapis.com/css2?family=Roboto:wght@400;700&family=Roboto+Condensed:wght@400&family=Questrial&family=Montserrat:wght@700&display=swap">
<style>
  :root {
    --stage-edge: #050505;
    --stage-mid: #6a6a6a;
    --brand-blue: #009ddd;
    --ink-black: #000000;
    --ink-grey: #7a7a7a;
    --divider-grey: #9a9a9a;
    --paper: #ffffff;
  }
  * { margin: 0; padding: 0; box-sizing: border-box; }
  html, body { width: 1200px; height: 900px; overflow: hidden; }
  body {
    position: relative;
    background: linear-gradient(90deg, var(--stage-edge) 0%, #2b2b2b 14%, var(--stage-mid) 50%, #2b2b2b 86%, var(--stage-edge) 100%);
    font-family: "Roboto", Arial, sans-serif;
  }
  .card { position: absolute; left: 225px; width: 750px; }

  /* Front card */
  .card-front { top: 12px; height: 430px; background: var(--paper); }
  .front-header {
    height: 193px; background: var(--ink-black);
    display: flex; align-items: center; justify-content: center;
  }
  .front-divider { height: 14px; background: var(--divider-grey); }
  .brand-name {
    font-family: "Roboto", Arial, sans-serif; font-weight: 700;
    font-size: 32px; color: var(--brand-blue); letter-spacing: 0.2px;
  }
  .person { position: absolute; left: 37px; top: 256px; }
  .person-name {
    font-family: "Questrial", sans-serif; font-size: 25px; color: var(--ink-black); line-height: 1;
  }
  .person-name .given {
    font-family: "Montserrat", sans-serif; font-weight: 700; color: var(--brand-blue); font-size: 23px;
  }
  .person-title {
    font-family: "Questrial", sans-serif; font-size: 15.5px; color: var(--ink-grey);
    margin-top: 6px; letter-spacing: 0.4px;
  }
  .address {
    position: absolute; left: 37px; top: 358px;
    font-family: "Roboto Condensed", sans-serif; font-size: 18px; color: var(--ink-grey); line-height: 25px;
  }
  .contact-list { position: absolute; left: 457px; top: 260px; list-style: none; }
  .contact-list li {
    display: flex; align-items: center; height: 30px;
    font-family: "Questrial", sans-serif; font-size: 19.5px; color: var(--ink-grey); letter-spacing: 0.6px;
  }
  .contact-list svg { width: 26px; height: 26px; margin-right: 9px; flex: none; }

  /* Back card */
  .card-back {
    top: 459px; height: 429px; background: var(--brand-blue);
    text-align: center;
  }
  .card-back .brand-name { color: var(--paper); display: block; margin-top: 222px; }
  .tagline {
    font-family: "Roboto", Arial, sans-serif; font-weight: 700; font-size: 22px;
    color: var(--ink-black); margin-top: 26px;
  }
</style>
</head>
<body>

<section class="card card-front">
  <header class="front-header">
    <span class="brand-name">RT Haverbrook &amp; Co. Inc</span>
  </header>
  <div class="front-divider"></div>

  <div class="person">
    <p class="person-name"><span class="given">Robert T</span> Haverbrook</p>
    <p class="person-title">Principal Consultant</p>
  </div>

  <p class="address">
    4817 Willow Crest Ln. San Diego CA 92847<br>
    Licences: CA 514728&nbsp; AZ 907465&nbsp; NV 0063512
  </p>

  <ul class="contact-list">
    <li>
      <svg viewBox="0 0 26 26" aria-hidden="true"><circle cx="13" cy="13" r="12" fill="var(--brand-blue)" stroke="#000" stroke-width="1.5"/><path d="M9 7l2.5-.5 1.5 3.5-1.5 1.2c.8 1.8 2 3 3.8 3.8L16.5 13.5 20 15l-.5 2.5c-5.5.5-11-5-10.5-10.5z" fill="#fff"/></svg>
      555 217 6400
    </li>
    <li>
      <svg viewBox="0 0 26 26" aria-hidden="true"><circle cx="13" cy="13" r="12" fill="var(--brand-blue)" stroke="#000" stroke-width="1.5"/><rect x="9" y="6.5" width="8" height="5" fill="#fff"/><rect x="7" y="11.5" width="12" height="6" rx="1" fill="#fff"/><rect x="9" y="17" width="8" height="3" fill="#fff"/></svg>
      555 217 6402
    </li>
    <li>
      <svg viewBox="0 0 26 26" aria-hidden="true"><circle cx="13" cy="13" r="12" fill="var(--brand-blue)" stroke="#000" stroke-width="1.5"/><rect x="9.5" y="5.5" width="7" height="15" rx="1.5" fill="#fff"/><rect x="10.7" y="7.5" width="4.6" height="9" fill="var(--brand-blue)"/></svg>
      555 217 6488
    </li>
    <li>
      <svg viewBox="0 0 26 26" aria-hidden="true"><circle cx="13" cy="13" r="12" fill="var(--brand-blue)" stroke="#000" stroke-width="1.5"/><rect x="6.5" y="8.5" width="13" height="9" fill="#fff"/><path d="M6.5 8.5l6.5 5 6.5-5M6.5 17.5l4.5-4M19.5 17.5l-4.5-4" fill="none" stroke="var(--brand-blue)" stroke-width="1"/></svg>
      rt@rthaverbrook-example.com
    </li>
    <li>
      <svg viewBox="0 0 26 26" aria-hidden="true"><circle cx="13" cy="13" r="12" fill="var(--brand-blue)" stroke="#000" stroke-width="1.5"/><g fill="none" stroke="#fff" stroke-width="1.2"><circle cx="13" cy="13" r="6.5"/><ellipse cx="13" cy="13" rx="3" ry="6.5"/><path d="M6.5 13h13M8 9.5h10M8 16.5h10"/></g></svg>
      rthaverbrook-example.com
    </li>
  </ul>
</section>

<section class="card card-back">
  <span class="brand-name">RT Haverbrook &amp; Co. Inc</span>
  <p class="tagline">Roofing Consultants and Contractors</p>
</section>

</body>
</html>
```